Atelier Vane Architecture business card

We need to update our business card. We do high end custom residential, hospitality, and wellness architecture. We focus on creating unique spaces and design around the five senses, believing that architecture's true impact is not on our surroundings, but within us. We would like to see designs are instill a sense of calm awe. They should be crisp, fresh, clean, authentic, & contemporary without being sterile, overworked, or harsh. White space is important. Alternative materials are an option if natural. We have created our own logo and would like designs to incorporate it. However, we are willing to see alternatives if the logo becomes a stumbling block and you have an alternate you suggest. Card must have the following information:
Atelier Vane Architecture, Inc.
742 Marbury Rd. NE Atlanta, GA 30319
Dominic K. Whitlow, AIA, NCARB, LEED AP BD+C
ateliervane.example

Target Market(s)

Higher net worth individuals with an appreciation for design, nature, sustainability,

Industry/Entity Type

Architect

Contact Information for Business Card

See above. The title of Owner or Architect is helpful but not necessary. Minimalism should trump additional information.

Font styles to use
Serif
Sans Serif

Requirements
Must have
• It should look professional. It must use logo
Should not have
• caligraphy, animals, anything that is cute,

```html
<!DOCTYPE html>
<html lang="en">
<head>
<meta charset="utf-8">
<title>Atelier Vane Architecture – Business Card</title>
<link rel="stylesheet" href="https://fonts.googleapis.com/css2?family=Arimo:wght@400&family=Marcellus&display=swap">
<style>
  :root {
    --backdrop: #d4d4d4;
    --card-dark-a: #323130;
    --card-dark-b: #454443;
    --card-light-a: #ebeaea;
    --card-light-b: #f7f7f7;
    --brand-green: #1f7a3e;
    --ink: #3a3a3a;
    --paper-text: #ffffff;
  }
  * { margin: 0; padding: 0; box-sizing: border-box; }
  html, body {
    width: 1167px; height: 1200px; overflow: hidden;
    background: var(--backdrop);
  }
  .canvas { position: relative; width: 1167px; height: 1200px; }

  .card {
    position: absolute; left: 165px;
    box-shadow: 0 2px 10px rgba(0,0,0,0.25);
  }
  .card--front {
    top: 111px; width: 796px; height: 439px;
    background: linear-gradient(135deg, var(--card-dark-a) 0%, var(--card-dark-b) 100%);
    display: flex; align-items: center; justify-content: center;
  }
  .card--back {
    top: 618px; width: 799px; height: 442px;
    overflow: hidden;
    background: linear-gradient(160deg, var(--card-light-a) 0%, var(--card-light-b) 100%);
  }

  .wordmark {
    font-family: "Marcellus", serif;
    color: var(--paper-text);
    font-size: 30px;
    letter-spacing: 0.32em;
    text-transform: uppercase;
    white-space: nowrap;
    margin-top: -16px;
    padding-left: 0.32em;
  }

  .rule-h {
    position: absolute; left: 86px; top: 225px;
    width: 666px; height: 1px; background: var(--ink);
  }
  .rule-v {
    position: absolute; left: 493px; top: 149px;
    width: 2px; height: 167px; background: var(--brand-green);
  }

  .person {
    position: absolute; right: 324px; top: 178px;
    text-align: right; font-family: "Arimo", sans-serif;
    white-space: nowrap;
  }
  .person__name {
    color: var(--brand-green);
    font-size: 35px; letter-spacing: 0.06em; line-height: 1;
  }
  .person__credentials {
    margin-top: 18px;
    color: var(--ink); font-size: 15px; letter-spacing: 0.1em;
  }

  .contact {
    position: absolute; left: 517px; top: 175px;
    width: 235px;
    font-family: "Arimo", sans-serif; color: var(--ink);
    font-size: 15px; letter-spacing: 0.04em;
    white-space: nowrap;
  }
  .contact__address { line-height: 20px; }
  .contact__list { list-style: none; margin-top: 14px; }
  .contact__item {
    display: flex; align-items: center; gap: 10px;
    height: 25px;
  }
  .contact__icon { width: 17px; height: 17px; flex: none; }
</style>
</head>
<body>
<main class="canvas">
  <section class="card card--front" aria-label="Card front">
    <p class="wordmark">Atelier Vane Architecture</p>
  </section>

  <section class="card card--back" aria-label="Card back">
    <div class="rule-h"></div>
    <div class="rule-v"></div>

    <div class="person">
      <p class="person__name">Dominic K. Whitlow</p>
      <p class="person__credentials">AIA, NCARB, LEED AP BD+C</p>
    </div>

    <div class="contact">
      <p class="contact__address">742 Marbury Rd. NE<br>Atlanta, GA 30319</p>
      <ul class="contact__list">
        <li class="contact__item">
          <svg class="contact__icon" viewBox="0 0 18 18" aria-hidden="true">
            <circle cx="9" cy="9" r="7.5" fill="none" stroke="#1f7a3e" stroke-width="1.4"/>
            <path d="M6.2 5.2l1.4-.3.9 2-.9.8a5 5 0 0 0 2.7 2.7l.8-.9 2 .9-.3 1.4c-3.6.4-7-3-6.6-6.6z" fill="#1f7a3e"/>
          </svg>
          <span>404 555 0187</span>
        </li>
        <li class="contact__item">
          <svg class="contact__icon" viewBox="0 0 18 18" aria-hidden="true">
            <rect x="1.5" y="4" width="15" height="10" fill="#1f7a3e"/>
            <path d="M1.5 4.5L9 10l7.5-5.5" fill="none" stroke="#f2f2f2" stroke-width="1.2"/>
          </svg>
          <span>dk@ateliervane.example</span>
        </li>
        <li class="contact__item">
          <svg class="contact__icon" viewBox="0 0 18 18" aria-hidden="true">
            <g fill="none" stroke="#1f7a3e" stroke-width="1.2">
              <circle cx="9" cy="9" r="7.5"/>
              <ellipse cx="9" cy="9" rx="3.3" ry="7.5"/>
              <path d="M1.5 9h15M3 5h12M3 13h12"/>
            </g>
          </svg>
          <span>www.ateliervane.example</span>
        </li>
      </ul>
    </div>
  </section>
</main>
</body>
</html>
```